Plastic Aesthetic and Reconstructive Surgery

I need a double sided luxurius Business Card, with a minimal, modern design focused on my job.
Besides my Name, Surname and contact information, the use of my initials (M and T) in free style combination as a logo will help.
In the one side all data written in English.
In the other side written in Greek if possible.
Please feel free to use the letter type and size you prefer.
Please use icons type and size and orientation you like.
The Name, Surname, occupation and the initials can be UV spotted.
You can use also in the background a texture or something that will make the card luxurious.
I would prefer pal colors.
Each side can have different colors or even better they can be reversed or inverted
As I have said you can use the wet sand color, light brown, dark brown, gold, light gold, white
Updates

Need extra days to review

i am waiting for some new ideas and some modifications from the designers. I need a couple of days extention of the period for the designers to post their modifications.

Target Market(s)

Patients who need a reconstructive intervention or surgery. Also people, mainly women, that they need aesthetic or cosmetic interventions to face or body

Contact Information for Business Card

Name and surname, occupation, member of an organization , mobile telephone number, Mail, Vela and Lumo accounts

Font styles to use
Script
Other font styles liked:
• Gabriola

Colors
FFC000
F8CF3A
FAE287
FDF2CF
FEFAEE

Requirements
Must have
• A free combination of my initials (M and T) as a logo
Nice to have
• Fade out with the background colors, UV spotted of the name, initials logo
Should not have
• Address

```html
<!DOCTYPE html>
<html lang="en">
<head>
<meta charset="utf-8">
<title>Markos Theodorou, MD, MSc — Business Card</title>
<link rel="stylesheet" href="https://fonts.googleapis.com/css2?family=Cinzel:wght@400;500&family=Montserrat:wght@400&family=Quattrocento+Sans:wght@400&display=swap">
<style>
  :root {
    --page: #ffffff;
    --sand: #a38b73;
    --ink: #141414;
    --paper: #ffffff;
    --rule-light: #f4efe9;
    --shadow: rgba(0, 0, 0, 0.28);
  }
  * { box-sizing: border-box; margin: 0; padding: 0; }
  html, body {
    width: 1200px; height: 1000px; overflow: hidden;
    background: var(--page);
  }
  .canvas { position: relative; width: 1200px; height: 1000px; }

  .card {
    position: absolute; left: 294px; width: 613px; height: 352px;
    border-radius: 22px;
    box-shadow: 0 40px 50px -20px var(--shadow), 0 12px 40px rgba(0,0,0,0.12);
  }
  .card--front { top: 124px; background: var(--sand); color: var(--paper); }
  .card--back  { top: 552px; background: var(--paper); color: var(--ink); }

  .monogram {
    position: absolute; display: flex; align-items: center; gap: 10px;
    font-family: "Cinzel", serif; font-weight: 400; line-height: 1;
  }
  .monogram__dot { width: 12px; height: 12px; border-radius: 50%; background: currentColor; }
  .card--front .monogram { left: 108px; top: 115px; font-size: 58px; }
  .card--back .monogram  { left: 448px; top: 110px; font-size: 50px; }

  .name {
    position: absolute; font-family: "Cinzel", serif; font-weight: 400;
    text-transform: uppercase;
  }
  .card--front .name { left: 263px; top: 95px; font-size: 27px; line-height: 34px; letter-spacing: 1.2px; }
  .card--back .name  { left: 56px; top: 102px; font-size: 22.5px; line-height: 29px; letter-spacing: 1.4px; }

  .rule { position: absolute; height: 0; }
  .card--front .rule { left: 40px; right: 30px; top: 256px; border-top: 1.5px solid var(--rule-light); }
  .card--back .rule  { left: 35px; right: 35px; top: 239px; border-top: 1.5px solid var(--sand); }

  .specialty {
    position: absolute; left: 0; right: 0; top: 271px; text-align: center;
    font-family: "Montserrat", sans-serif; font-size: 11px; letter-spacing: 2.6px;
    text-transform: uppercase; padding-left: 12px;
  }

  .contact {
    position: absolute; left: 56px; top: 267px;
    font-family: "Quattrocento Sans", sans-serif; font-size: 14px; line-height: 19px;
    letter-spacing: 0.3px;
  }

  .social {
    position: absolute; right: 50px; top: 279px; display: flex; gap: 8px;
    font-family: "Quattrocento Sans", sans-serif; font-size: 13px; color: var(--sand);
  }
</style>
</head>
<body>
<main class="canvas">
  <section class="card card--front" aria-label="Card front">
    <div class="monogram"><span class="monogram__dot"></span><span>MT</span></div>
    <h1 class="name">Markos<br>Theodorou,<br>MD, MSc</h1>
    <div class="rule"></div>
    <p class="specialty">Plastic Reconstructive and Aesthetic Surgery</p>
  </section>

  <section class="card card--back" aria-label="Card back">
    <h2 class="name">Markos<br>Theodorou,<br>MD, MSc</h2>
    <div class="monogram"><span class="monogram__dot"></span><span>MT</span></div>
    <div class="rule"></div>
    <p class="contact">+30 694 321 8870<br>m.theodorou.md@mailbox.com</p>
    <p class="social"><span>Vela</span><span>Lumo</span></p>
  </section>
</main>
</body>
</html>
```